Need help refining Tallbergsgillet

Hi We need help with the refining of overall design and details of our homepage design Tallbergsgillet. See attached files.

Attached files:
homepage.psd - file you can use to work from.
homepage.png – quick notes on thoughts of the design
logo.psd (smart object) – The logo should be in gold.
social media elements.png - what type of data that needs design in the feed

What we need:
Something is missing with the overall design as well as detailed design for our social media feed. We don’t know what and hope you can solve this for us.

The homepage:
Our main page include a selfloading blogfeed combined with Vendraly- and Instagramfeed.

Fonts:
So far I´ve used Roboto regular, and Georgia, but feel free to use other fonts if you find better suited

Among others, we need a better detailed design that works better with the overall design.

Se attached sample image (social_mediafeed.png) what types of data we get from Vendraly in our feed. Feel free to redesign the elements of this data.

Headerlinks:
Even though we only have one page, there should be place for links to other pages as well which will load below the header.

Social media follow: Place for social media follow links/icons/buttons in style with rest of the design. Maybe at top grey border? We use Glimtora and Vendraly in style with rest of the design.

Colors:
The logo should be in gold, and use of "goldish" colors troughout the page.
Also blue elements troughout the page

Logo in gold/goldish color
Blue elements # 13416c (or similar color that works well in the design)

Target Market(s)

Wellness, fitness, spa and food, Exclusive

Number of Pages Required

1 page

Font styles to use
Serif
Sans Serif
Script
Other font styles liked:
• Roboto, Georgia

Requirements
Must have
• Better overall design that feel harmonic.
• Better design of blog and social media feeds (se all attached images)
• Nice clean design, easy on the eye
• Colors on theme: Gold + blue

```html
<!DOCTYPE html>
<html lang="sv">
<head>
<meta charset="utf-8">
<title>Tallbergsgillet</title>
<link href="https://fonts.googleapis.com/css2?family=Montserrat:wght@400;500;600&family=Open+Sans:wght@400;600&family=Playfair+Display:ital@1&family=Libre+Baskerville&display=swap" rel="stylesheet">
<style>
:root{
  --gold:#c9a24a;
  --gold-light:#e3c27a;
  --blue:#13416c;
  --ink:#333;
  --muted:#777;
  --page:#f2f2f2;
  --topbar:#ebebeb;
  --line:#d8d8d8;
  --footer:#e6e6e6;
  --bottom:#555;
}
*{box-sizing:border-box;margin:0;padding:0}
html,body{width:1200px;height:3180px;overflow:hidden}
body{position:relative;background:var(--page);font-family:"Open Sans",Arial,sans-serif;color:var(--ink)}
.abs{position:absolute}
h1,h2,h3{font-weight:400}
/* top bar */
.topbar{left:0;top:0;width:1200px;height:28px;background:var(--topbar)}
.follow{left:196px;top:7px;display:flex;gap:16px;font-family:"Montserrat",sans-serif;font-size:10px;color:#555;z-index:2}
.follow span{display:flex;align-items:center;gap:6px}
.follow span::before{content:"";width:11px;height:11px;border:1.5px solid var(--gold);border-radius:2px;display:block}
.account{right:205px;top:6px;display:flex;gap:22px;font-size:10px;color:#555}
.account span::before{content:"";display:inline-block;width:8px;height:8px;border:1.5px solid var(--gold);border-radius:50%;margin-right:6px;vertical-align:-1px}
/* header */
.header{left:0;top:28px;width:1200px;height:114px;background:#fff}
.header-rule{left:0;top:98px;width:1200px;height:2px;background:var(--blue)}
.nav{top:82px;display:flex;font-family:"Montserrat",sans-serif;font-size:11px;letter-spacing:.3px;color:#333;z-index:2}
.nav a{color:inherit;text-decoration:none}
.nav .active{color:var(--gold)}
.logo{left:510px;top:38px;width:180px;height:90px;background:#fff;text-align:center;padding-top:6px;z-index:3}
.logo-mark{width:34px;height:34px;border:2px solid var(--gold);border-radius:50%;margin:0 auto 8px}
.logo-name{font-family:"Libre Baskerville",Georgia,serif;color:var(--gold);font-size:15px;letter-spacing:.5px}
.dropdown{left:865px;top:110px;width:135px;background:#fff;box-shadow:0 2px 6px rgba(0,0,0,.15);font-family:"Montserrat",sans-serif;font-size:9px;color:#888;z-index:5}
.dropdown div{height:34px;line-height:34px;padding-left:12px;border-bottom:1px solid #eee}
.dropdown .current{background:var(--gold-light);color:#fff}
/* hero */
.hero{left:0;top:142px;width:1200px;height:430px;background:
  radial-gradient(ellipse 45% 35% at 70% 55%,rgba(160,120,80,.55),transparent 70%),
  radial-gradient(ellipse 60% 30% at 30% 38%,rgba(110,140,170,.6),transparent 70%),
  linear-gradient(180deg,#b7c6d4 0%,#7e97ad 22%,#5d7288 40%,#55604f 62%,#7a6345 82%,#5a4630 100%)}
.hero-box{left:197px;top:278px;width:303px;height:167px;background:rgba(40,48,58,.5);border-left:3px solid var(--gold)}
.hero-title{left:225px;top:290px;font-family:"Montserrat",sans-serif;font-size:50px;color:#fff;font-weight:400}
.hero-sub{left:226px;top:360px;font-size:16px;color:#fff}
.btn-gold{left:226px;top:394px;width:98px;height:32px;background:var(--gold);color:#fff;font-family:"Montserrat",sans-serif;font-size:11px;text-align:center;line-height:32px}
.arrow{top:318px;width:46px;height:46px;display:flex;align-items:center;justify-content:center}
.arrow.prev{left:0;background:#fff}
.arrow.next{right:0;background:var(--gold-light)}
/* offers */
.section-title{left:0;top:612px;width:1200px;text-align:center;font-family:"Montserrat",sans-serif;font-size:26px;color:#444}
.section-title em{font-style:normal;color:var(--gold)}
.card{top:683px;width:250px;height:320px;background:#fff;box-shadow:0 1px 4px rgba(0,0,0,.12)}
.card-img{position:absolute;left:0;top:0;width:250px;height:186px}
.card-img .overlay{position:absolute;left:16px;top:14px;color:#fff;font-family:"Libre Baskerville",Georgia,serif;font-size:17px}
.card-img .overlay small{display:block;font-size:13px;margin-top:16px}
.card-img .overlay b{font-family:"Montserrat",sans-serif;font-weight:500;font-size:34px}
.card-img .overlay b i{font-style:normal;font-size:13px}
.card-name{position:absolute;left:16px;top:206px;font-family:"Montserrat",sans-serif;font-size:12px;font-weight:500;letter-spacing:.3px}
.card-text{position:absolute;left:16px;top:226px;font-size:12px;color:#555}
.btn-blue{position:absolute;left:16px;top:268px;width:98px;height:32px;background:var(--blue);color:#fff;font-family:"Montserrat",sans-serif;font-size:10px;text-align:center;line-height:32px}
/* panels */
.panel{left:157px;width:882px;background:#fff;box-shadow:0 1px 4px rgba(0,0,0,.08)}
.post{top:1062px;height:878px}
.post-title{position:absolute;left:0;top:26px;width:100%;text-align:center;font-family:"Montserrat",sans-serif;font-size:28px;color:#333}
.post-meta{position:absolute;left:0;top:76px;width:100%;text-align:center;font-size:10px;color:#888;letter-spacing:.3px}
.post-meta b{font-weight:400;color:var(--gold)}
.post-img{position:absolute;left:38px;top:115px;width:810px;height:409px;background:
  radial-gradient(ellipse 30% 40% at 45% 35%,rgba(40,45,50,.8),transparent 70%),
  radial-gradient(ellipse 22% 30% at 20% 70%,rgba(215,170,140,.7),transparent 70%),
  radial-gradient(ellipse 40% 35% at 80% 70%,rgba(90,200,225,.8),transparent 70%),
  linear-gradient(160deg,#e9eff2 0%,#a9dcea 45%,#7fc6d8 70%,#cfe8ef 100%)}
.post-body{position:absolute;left:38px;top:568px;width:810px;font-size:11.5px;line-height:20px;color:#666}
.dropcap{float:left;font-family:"Montserrat",sans-serif;font-size:54px;line-height:50px;color:#222;margin-right:6px;font-weight:600}
.post-h2{position:absolute;left:38px;top:652px;font-family:"Montserrat",sans-serif;font-size:22px;font-weight:500;color:#222}
.post-body2{position:absolute;left:38px;top:696px;width:810px;font-size:11.5px;line-height:21px;color:#666}
.post-foot{position:absolute;left:38px;top:789px;width:810px;height:38px;border-top:2px solid var(--line);border-bottom:2px solid var(--line);font-family:"Montserrat",sans-serif;font-size:11px;display:flex;align-items:center;gap:26px;padding-left:2px}
.post-foot span{display:flex;align-items:center;gap:8px}
.read-on{margin-left:auto;font-family:"Playfair Display",Georgia,serif;font-style:italic;color:var(--gold);font-size:14px}
/* feed items */
.feed{height:365px}
.feed-head{position:absolute;left:38px;top:30px;display:flex;align-items:center;gap:12px;font-family:"Montserrat",sans-serif;font-size:17px;color:#333}
.feed-icon{width:24px;height:24px;border-radius:50%;background:var(--gold)}
.feed-meta{position:absolute;left:38px;top:70px;font-size:10px;color:var(--gold)}
.feed-lead{position:absolute;left:38px;top:98px;width:390px;font-size:14px;line-height:21px;color:#777}
.feed-lead .first{font-size:22px;color:#333}
.feed-text{position:absolute;left:38px;width:390px;font-size:13px;line-height:20px;color:#777}
.feed-more{position:absolute;left:38px;font-family:"Montserrat",sans-serif;font-size:11px;font-weight:600;display:flex;align-items:center;gap:6px}
.feed-img{position:absolute;left:481px;top:34px;width:359px;height:288px}
/* footer */
.footer{left:0;top:2798px;width:1200px;height:331px;background:var(--footer)}
.vendraly-box{left:159px;top:2826px;width:254px;height:280px;background:#fff}
.vb-head{position:absolute;left:14px;top:16px;display:flex;align-items:center;gap:10px;font-size:12px;color:var(--gold)}
.vb-head i{width:22px;height:22px;border-radius:50%;background:var(--blue);display:block}
.vb-date{position:absolute;left:46px;top:42px;font-size:8px;color:#888}
.vb-text{position:absolute;left:14px;top:68px;width:226px;font-size:9px;line-height:13px;color:#666}
.vb-img{position:absolute;left:24px;top:136px;width:206px;height:112px;background:
  radial-gradient(ellipse 35% 40% at 50% 55%,rgba(200,170,120,.8),transparent 70%),
  linear-gradient(160deg,#e2e6d8,#8a9a6e 60%,#6f7e52)}
.vb-bar{position:absolute;left:0;bottom:0;width:254px;height:24px;background:var(--blue);color:#fff;font-family:"Montserrat",sans-serif;font-size:10px;line-height:24px;padding-left:12px}
.foot-title{top:2840px;font-family:"Montserrat",sans-serif;font-size:12px;font-weight:500;border-bottom:1px solid #999;padding-bottom:6px}
.grid{left:485px;top:2870px;display:grid;grid-template-columns:repeat(3,85px);gap:4px}
.grid div{height:76px}
.about-logo{left:820px;top:2880px;width:206px;text-align:center}
.about-logo .logo-mark{border-color:#333;width:28px;height:28px}
.about-logo .logo-name{color:#333;font-size:12px}
.about-text{left:820px;top:2950px;width:206px;font-size:10px;line-height:14px;color:#555}
.bottom{left:0;top:3129px;width:1200px;height:51px;background:var(--bottom);color:#ddd;font-family:"Montserrat",sans-serif;font-size:9px;text-align:center;line-height:51px;letter-spacing:.5px}
</style>
</head>
<body>

<div class="abs topbar"></div>
<div class="abs follow"><span>Vendraly</span><span>Glimtora</span></div>
<div class="abs account"><span>Bli medlem</span><span>Medlemslogin</span></div>

<header class="abs header"></header>
<div class="abs header-rule"></div>
<nav class="abs nav" style="left:195px"><a style="margin-right:60px">HEM</a><a style="margin-right:60px">GILLESRESOR</a><a class="active">INSPIRATION</a></nav>
<nav class="abs nav" style="left:718px"><a style="margin-right:40px">MEDLEMSERBJUDANDEN</a><a style="margin-right:32px">OM</a><a>KONTAKTA OSS</a></nav>
<div class="abs logo"><div class="logo-mark"></div><div class="logo-name">TALLBERGSGILLET</div></div>

<section class="abs hero" role="img" aria-label="Fotografi av slingrande bergsväg i dimmigt berglandskap"></section>
<div class="abs dropdown"><div class="current">TALLBERGSGILLET</div><div>GILLESBILJETTER</div><div>RESOR</div></div>
<div class="abs hero-box"></div>
<div class="abs hero-title">Featured</div>
<div class="abs hero-sub">liten beskrivning av post</div>
<div class="abs btn-gold">LÄS MER</div>
<div class="abs arrow prev"><svg width="12" height="12" viewBox="0 0 12 12"><path d="M8 1 3 6l5 5" fill="none" stroke="#999" stroke-width="1.5"/></svg></div>
<div class="abs arrow next"><svg width="12" height="12" viewBox="0 0 12 12"><path d="M4 1l5 5-5 5" fill="none" stroke="#fff" stroke-width="1.5"/></svg></div>

<h2 class="abs section-title">Tallbergsgillets <em>Medlemserbjudanden</em></h2>

<article class="abs card" style="left:195px">
  <div class="card-img" role="img" aria-label="Fotografi av stadsgata med ljusspår i skymning" style="background:radial-gradient(ellipse 50% 40% at 50% 85%,rgba(240,170,80,.9),transparent 70%),linear-gradient(180deg,#2a4a7a,#4a5d80 45%,#b87a3e)">
    <div class="overlay">Hälsa &amp; skönhet AB<small>Motionera mera</small><b>30%<i> Rabatt</i></b></div></div>
  <div class="card-name">HÄLSA &amp; SKÖNHET AB</div>
  <div class="card-text">En kort rubrik på erbjudandet</div>
  <div class="btn-blue">LÄS MER</div>
</article>
<article class="abs card" style="left:477px">
  <div class="card-img" role="img" aria-label="Fotografi av skyskrapor i kvällsljus" style="background:radial-gradient(ellipse 40% 50% at 70% 60%,rgba(200,170,120,.6),transparent 70%),linear-gradient(180deg,#4a6d98,#2e4566 55%,#1e2b3a)">
    <div class="overlay">Hälsa &amp; skönhet AB<small>Motionera mera</small><b>30%<i> Rabatt</i></b></div></div>
  <div class="card-name">HÄLSA &amp; SKÖNHET AB</div>
  <div class="card-text">En kort rubrik på erbjudandet</div>
  <div class="btn-blue">LÄS MER</div>
</article>
<article class="abs card" style="left:761px">
  <div class="card-img" role="img" aria-label="Flygfoto över kuststad och hav" style="background:radial-gradient(ellipse 45% 40% at 75% 30%,rgba(210,190,160,.75),transparent 70%),linear-gradient(160deg,#5c7f93,#2f8aa6 55%,#1f6f86)">
    <div class="overlay">Hälsa &amp; skönhet AB<small>Motionera mera</small><b>30%<i> Rabatt</i></b></div></div>
  <div class="card-name">HÄLSA &amp; SKÖNHET AB</div>
  <div class="card-text">En kort rubrik på erbjudandet</div>
  <div class="btn-blue">LÄS MER</div>
</article>

<article class="abs panel post">
  <h1 class="post-title">En trevlig rubrik på ditt blogginlägg</h1>
  <div class="post-meta">22 OKTOBER, 2016 &nbsp;|&nbsp; AV TALLBERGSGILLET &nbsp;|&nbsp; 0 KOMMENTARER &nbsp;|&nbsp; <b>◆</b> SPA, LIVSNJUTNING, YOGA</div>
  <div class="post-img" role="img" aria-label="Fotografi av kvinna som badar i turkost geotermiskt bad bland lavaklippor"></div>
  <p class="post-body"><span class="dropcap">E</span>ed dui consectetur, eleifend nibh et, ultricies justo. Vivamus luctus elit ac lacus placerat laoreet vel at lacus. Sed a molestie ex. Vestibulum ac varius libero. Fusce sollicitudin non tellus lacinia molestie. Sed rhoncus dui a sem accumsan, nec scelerisque augue suscipit. Aliquam eget justo odio. Maecenas in molestie tortor, eu tristique ligula. Suspendisse vulputate urna ut elit iaculi varius.</p>
  <h3 class="post-h2">Rubrik 2</h3>
  <p class="post-body2">Quisque laoreet nisi purus. Suspendisse sit amet nulla dolor. Morbi felis sem, condimentum fermentum ullamcorper a, auctor rhoncus justo.<br>Morbi tempus sit amet ante eu placerat. In nec odio ac dui molestie iaculis eu nec tellus. Etiam venenatis sed dolor in commodo.<br>Sed venenatis iaculis faucibus. Quisque eleifend a leo eu sodales.</p>
  <div class="post-foot">
    <span><svg width="14" height="14" viewBox="0 0 14 14"><circle cx="11" cy="3" r="2" fill="var(--gold)"/><circle cx="3" cy="7" r="2" fill="var(--gold)"/><circle cx="11" cy="11" r="2" fill="var(--gold)"/><path d="M11 3 3 7l8 4" fill="none" stroke="var(--gold)"/></svg>DELA</span>
    <span><svg width="14" height="13" viewBox="0 0 14 13"><path d="M1 1h12v8H6l-3 3V9H1z" fill="var(--gold)"/></svg>KOMMENTERA</span>
    <span class="read-on">Continuer la lecture →</span>
  </div>
</article>

<article class="abs panel feed" style="top:1972px">
  <div class="feed-head"><span class="feed-icon"></span>GLIMTORA</div>
  <div class="feed-meta">13 OKTOBER, 2016 &nbsp;|&nbsp; AV TALLBERGSGILLET</div>
  <p class="feed-lead"><span class="first">N</span>i vet den där känslan när man kommer in på hotellrummet för första gången och vet att man är långledig tillsammans hela helgen. Den känslan...<br><br>#långledig #välmående #momentsofhappiness #tallbergsgillet</p>
  <div class="feed-more" style="top:272px">LÄS MER <svg width="18" height="18" viewBox="0 0 18 18"><circle cx="9" cy="9" r="7.5" fill="none" stroke="#222" stroke-width="1.5"/><path d="M7.5 5.5 11 9l-3.5 3.5" fill="none" stroke="#222" stroke-width="1.5"/></svg></div>
  <div class="feed-img" role="img" aria-label="Fotografi av bäddad hotellsäng med vägglampor" style="background:radial-gradient(ellipse 60% 25% at 50% 62%,rgba(255,255,255,.9),transparent 70%),linear-gradient(180deg,#c2ab8f 0%,#d9cbb8 35%,#eee8e0 60%,#9c7a62 85%,#6e4f3c)"></div>
</article>

<article class="abs panel feed" style="top:2370px">
  <div class="feed-head"><span class="feed-icon"></span>VENDRALY</div>
  <div class="feed-meta">13 OKTOBER, 2016 &nbsp;|&nbsp; AV TALLBERGSGILLET</div>
  <p class="feed-lead"><span class="first">B</span>oosta ditt immunförsvar!</p>
  <p class="feed-text" style="top:130px">Skiva ingefära och citron och häll het vatten över. Ingefära är kroppens bästa vän som ökar både blodcirkulation och ämnesomsättningen. Den är antiinflammatorisk och motverkar både migrän och problem med lederna. Citron renar kroppen på gifter, stärker immunförsvaret, renar huden och ger energi. Denna välgörande dryck är full av antioxidanter som stärker kroppen. En god morgonvana för att boosta det friska.</p>
  <div class="feed-more" style="top:288px">LÄS MER <svg width="18" height="18" viewBox="0 0 18 18"><circle cx="9" cy="9" r="7.5" fill="none" stroke="#222" stroke-width="1.5"/><path d="M7.5 5.5 11 9l-3.5 3.5" fill="none" stroke="#222" stroke-width="1.5"/></svg></div>
  <div class="feed-img" style="top:32px;height:290px;background:radial-gradient(ellipse 45% 35% at 75% 70%,rgba(240,190,40,.9),transparent 70%),radial-gradient(ellipse 40% 40% at 20% 15%,rgba(255,235,200,.9),transparent 70%),linear-gradient(150deg,#e9c996,#9a7a52 45%,#6b5a48 75%,#3f342a)" role="img" aria-label="Fotografi av gul taxi på solig stadsgata"></div>
</article>

<footer class="abs footer"></footer>
<div class="abs vendraly-box">
  <div class="vb-head"><i></i>Tallbergsgillet</div>
  <div class="vb-date">JANUARI 20, 2016 &nbsp; 26</div>
  <p class="vb-text">Boosta ditt immunförsvar!<br>Skiva ingefära och citron och häll het vatten över. Ingefära är kroppens bästa vän som ökar blodets cirkulation och ämnesomsättningen.</p>
  <div class="vb-img" role="img" aria-label="Fotografi av kopp med ingefärsdryck och citron"></div>
  <div class="vb-bar">VENDRALY.COM</div>
</div>
<div class="abs foot-title" style="left:485px;width:268px">GLIMTORA POSTS</div>
<div class="abs grid" role="img" aria-label="Rutnät med nio små inläggsfotografier">
  <div style="background:linear-gradient(150deg,#a5806c,#6e5246)"></div><div style="background:linear-gradient(150deg,#9aa860,#5f6e3a)"></div><div style="background:linear-gradient(150deg,#d2b27c,#8e7450)"></div>
  <div style="background:linear-gradient(150deg,#56687a,#263340)"></div><div style="background:linear-gradient(150deg,#c4bca4,#847c66)"></div><div style="background:linear-gradient(150deg,#6a8a4e,#34502a)"></div>
  <div style="background:linear-gradient(150deg,#3f8a74,#1e3a3a)"></div><div style="background:linear-gradient(150deg,#e0bc92,#a07a56)"></div><div style="background:linear-gradient(150deg,#e39a4a,#6a3a1e)"></div>
</div>
<div class="abs foot-title" style="left:820px;width:206px">ABOUT US</div>
<div class="abs about-logo"><div class="logo-mark"></div><div class="logo-name">TALLBERGSGILLET</div></div>
<p class="abs about-text">Nascetur vel massa enim iundium nec in phasellus vel nisi nec penatibus. Duis phasellus ut! Amet risus ultricies integer elementum natoque ec tincidunt risus adipiscing. Vel massa enim iundium nec in phasellus.</p>
<div class="abs bottom">© 2016 COPYRIGHTS. ALL RIGHT RESERVED.</div>

</body>
</html>
```